Design to promote Vacation Tune Workshop Series for Kids

We are a small local music school in need of a poster design to promote our new Vacation Tune Workshop Series (sort of like a music camp) for the January 2013 Summer Break here in Sydney, Australia.

We generally teach students private instruments (e.g piano, guitar, bass, singing, drums, trumpet and theory) and offer group classes for Glee Club and Group Guitar.

The proposed Vacation Tune Workshop Series goes for 1 week and is 'Jam Packed' with lots of fun musical activities, workshops and musical experiences.

It's called 'Turn The Tunes Loose' and is designed for Kids aged 7 - 12 yrs of age.

We would like an A3 size poster to be designed and an A6 size flyer which compliments the poster. If you're able to also resize the A3 size poster to A4 that'll be great. The successful candidate can do that once the final design is confirmed.

The look and feel should be 'Summer', fun, musical, hip and targeted at young parents aged 28 - 50yrs old. These parents are generally professionals living in a creative area of Sydney.

Text to be included as follows:

'TURN THE TUNES LOOSE'
A Fun Jam Packed Vacation Tune Workshop Series for the Summer Break

Designed for Kids 7 - 12 years old

14 - 18 January, 2013
NEWTOWN

No experience necessary

INSTRUMENTAL DISCOVERY Learn and play a variety of musical instruments
SONG WRITING Write your own songs
BEAT BOXING Learn to beat box and rap
MUSIC GAMES Join in a number of fun musical games and activities
GLEE Do some singing (no problems if you've never tried)
MUSIC TECHNOLOGY Learn about music technology and how to record/produce songs
HAVE FUN!

EARLY BIRD REGISTRATION: $280 per child (when you enrol by 14 December, 2012)

COST: $300 per child
*discounts apply when enrolling 2 or more kids

Goes from Monday - Friday, 9:00am - 3:00pm

ENROL ONLINE NOW
www.brightkeysounds.com.au
Or call 02 7419 2856 / 0438 967 204

For enquiries or more info visit our website or email info@brightkeysounds.com.au

Bright Key Sound School
Unit 4B, 19 Harlow Street, Newtown (enter via Pembrick Ave)

Target Market(s)

Parents of children aged 7 - 12 yrs. They would be around 25 - 50 yrs old

Industry/Entity Type

School

Requirements
Must have
• Must include our company logo - there are two versions which you can pick from to use.

```html
<!DOCTYPE html>
<html lang="en">
<head>
<meta charset="utf-8">
<title>Turn The Tunes Loose – Vacation Tune Workshop Series</title>
<link href="https://fonts.googleapis.com/css2?family=Bowlby+One&family=Signika:wght@300;400;600;700&display=swap" rel="stylesheet">
<style>
  :root{
    --header-bg:#f1f1f1;
    --band-red:#e4573f;
    --panel-amber:#f7bd5e;
    --panel-edge:#eab055;
    --ink:#555555;
    --title-grey:#6e6a5f;
    --title-red:#e4573f;
    --brand-teal:#4bbfcf;
    --brand-orange:#f0703a;
    --date-top:#dde9d6;
    --date-bottom:#b3d5b5;
    --icon-tone:#e3a84f;
    --white:#ffffff;
  }
  *{margin:0;padding:0;box-sizing:border-box}
  html,body{width:848px;height:1200px;overflow:hidden;background:var(--band-red)}
  .poster{position:relative;width:848px;height:1200px;background:var(--band-red);font-family:"Signika",sans-serif;color:var(--ink)}
  .masthead{position:absolute;left:0;top:0;width:848px;height:133px;background:var(--header-bg);display:flex;align-items:center;justify-content:center;gap:16px}
  .brand-name{font-family:"Signika",sans-serif;font-weight:600;font-size:44px;color:var(--brand-teal);letter-spacing:-0.5px}
  .brand-dot{width:58px;height:58px;border-radius:50%;background:var(--brand-orange)}
  .feature-panel{position:absolute;left:14px;top:150px;width:816px;height:818px;background:var(--panel-amber);border:2px solid var(--panel-edge)}
  .headline{position:absolute;left:0;width:848px;text-align:center;font-family:"Bowlby One",sans-serif;white-space:nowrap;line-height:1;color:var(--title-grey)}
  .headline--one{top:160px;font-size:112px;letter-spacing:2px}
  .headline--two{top:272px;font-size:94px;letter-spacing:1px}
  .headline .accent{color:var(--title-red)}
  .tagline{position:absolute;left:0;top:384px;width:848px;text-align:center;font-size:24px;font-weight:400}
  .date-card{position:absolute;left:68px;top:450px;width:208px;height:194px;border:4px solid var(--ink);border-radius:9px;overflow:hidden;background:var(--date-top)}
  .date-days{height:124px;display:flex;align-items:center;justify-content:center;font-size:62px;font-weight:700}
  .date-month{height:66px;background:var(--date-bottom);text-align:center;padding-top:2px}
  .date-month strong{display:block;font-size:28px;font-weight:600;line-height:34px}
  .date-month span{display:block;font-size:18px;font-weight:600;line-height:20px}
  .location{position:absolute;left:310px;top:452px;width:240px;text-align:center}
  .location svg{display:block;margin:0 auto}
  .location-name{font-size:46px;font-weight:700;line-height:1;margin-top:8px}
  .early-bird{position:absolute;left:560px;top:442px;width:246px;text-align:center}
  .early-bird h2{font-size:40px;font-weight:700;line-height:44px}
  .early-bird h3{font-size:32px;font-weight:700;line-height:38px}
  .early-bird .price{font-size:37px;font-weight:400;line-height:46px}
  .early-bird .deadline{font-size:20px;font-weight:400;letter-spacing:2px;line-height:25px}
  .audience{position:absolute;left:0;top:654px;width:848px;text-align:center;font-size:27px}
  .audience strong{font-weight:700}
  .activities{position:absolute;left:0;top:720px;width:848px;list-style:none}
  .activity{display:flex;align-items:baseline;height:31px}
  .activity-name{width:374px;text-align:right;font-size:20px;font-weight:700;letter-spacing:2.4px}
  .activity-desc{margin-left:12px;font-size:15px;font-weight:400}
  .icon-strip{position:absolute;top:910px;height:50px;border-radius:6px;background:var(--icon-tone)}
  .icon-strip--left{left:48px;width:182px}
  .icon-strip--right{left:552px;width:250px}
  .have-fun{position:absolute;left:300px;top:915px;width:244px;text-align:center;font-size:30px;font-weight:700}
  .footer-cost{position:absolute;left:150px;top:990px;width:250px;text-align:right;color:var(--white);font-size:15px;font-weight:300;line-height:20px}
  .footer-enrol{position:absolute;left:446px;top:990px;width:380px;color:var(--white);font-size:15px;font-weight:300;line-height:20px}
  .footer-address{position:absolute;left:0;top:1088px;width:848px;text-align:center;color:var(--white);font-size:15px;font-weight:300;line-height:20px}
</style>
</head>
<body>
<main class="poster">
  <header class="masthead">
    <span class="brand-name">Bright Key Sounds</span>
    <span class="brand-dot"></span>
  </header>

  <div class="feature-panel"></div>

  <h1>
    <span class="headline headline--one">TURN THE</span>
    <span class="headline headline--two"><span class="accent">TUNES</span> LOOSE</span>
  </h1>
  <p class="tagline">A Fun Jam Packed Vacation Tune Workshop Series for the Summer Break</p>

  <div class="date-card">
    <div class="date-days">14-18</div>
    <div class="date-month"><strong>January</strong><span>2013</span></div>
  </div>

  <div class="location">
    <svg width="124" height="110" viewBox="0 0 124 110" aria-hidden="true">
      <ellipse cx="62" cy="88" rx="58" ry="20" fill="var(--date-top)" stroke="var(--ink)" stroke-width="4"/>
      <rect x="48" y="4" width="28" height="58" rx="14" fill="var(--ink)"/>
      <polygon points="30,48 94,48 62,86" fill="var(--ink)"/>
    </svg>
    <div class="location-name">NEWTOWN</div>
  </div>

  <div class="early-bird">
    <h2>EARLY BIRD</h2>
    <h3>REGISTRATION</h3>
    <p class="price">$280 per child</p>
    <p class="deadline">when you enrol by<br>14 December, 2012</p>
  </div>

  <p class="audience">Designed for <strong>Kids 7 - 12</strong> years old // No experience necessary</p>

  <ul class="activities">
    <li class="activity"><span class="activity-name">INSTRUMENTAL DISCOVERY</span><span class="activity-desc">Learn and play a variety of musical instruments</span></li>
    <li class="activity"><span class="activity-name">SONG WRITING</span><span class="activity-desc">Write your own songs</span></li>
    <li class="activity"><span class="activity-name">BEAT BOXING</span><span class="activity-desc">Learn to beat box and rap</span></li>
    <li class="activity"><span class="activity-name">MUSIC GAMES</span><span class="activity-desc">Join in a number of fun musical games and activities</span></li>
    <li class="activity"><span class="activity-name">GLEE</span><span class="activity-desc">Do some singing (no problems if you've never tried)</span></li>
    <li class="activity"><span class="activity-name">MUSIC TECHNOLOGY</span><span class="activity-desc">Learn about music technology and how to record/produce songs</span></li>
  </ul>

  <div class="icon-strip icon-strip--left" role="img" aria-label="Small icons of a guitar, a sun, a keyboard and a drum"></div>
  <p class="have-fun">HAVE FUN!</p>
  <div class="icon-strip icon-strip--right" role="img" aria-label="Small icons of a cap, a microphone, sunglasses and a trumpet"></div>

  <div class="footer-cost">
    COST: $300 per child<br>
    (discounts apply when<br>
    enrolling 2 or more kids)<br>
    Goes from Monday - Friday,<br>
    9:00am - 3:00pm
  </div>
  <div class="footer-enrol">
    ENROL ONLINE NOW<br>
    www.brightkeysounds.com.au<br>
    Or call 02 7419 2856 / 0438 967 204<br>
    For enquiries or more info visit our website or email<br>
    info@brightkeysounds.com.au
  </div>
  <div class="footer-address">
    Bright Key Sound School<br>
    Unit 4B, 19 Harlow Street, Newtown (enter via Pembrick Ave)
  </div>
</main>
</body>
</html>
```